Criação de Papelaria (6 itens) para Lumiar & Castelo
A empresa queria:
" EMPRESA FAMILIAR PRODUTORA DE GRÃOS hA 34 ANOS NO MERCADO, PIONEIRA EM IRRIGAÇÃO TIPO PIVO CENTRAL. "

```html
<!DOCTYPE html>
<html lang="pt-BR">
<head>
<meta charset="utf-8">
<title>Assinatura de e-mail – Lumiar &amp; Castelo</title>
<link href="https://fonts.googleapis.com/css2?family=Montserrat:wght@400;500;600&display=swap" rel="stylesheet">
<style>
  :root {
    --bg: #ececec;
    --taupe: #857b71;
    --gold: #b39457;
    --white: #ffffff;
    --ink: #2b2b2b;
    --ink-soft: #4a4a4a;
  }
  * { margin: 0; padding: 0; box-sizing: border-box; }
  html, body {
    width: 1200px; height: 1200px; overflow: hidden;
    background: var(--bg);
    font-family: "Montserrat", sans-serif;
  }
  .signature {
    position: absolute;
    left: 50px; top: 468px;
    width: 1100px; height: 264px;
    display: flex;
    background: var(--white);
    box-shadow: 0 4px 14px rgba(0,0,0,.12);
  }
  .brand-panel {
    width: 570px; height: 100%;
    background: var(--taupe);
    display: flex; align-items: center; justify-content: center;
    gap: 26px;
  }
  .brand-dot {
    width: 46px; height: 46px; border-radius: 50%;
    background: var(--gold);
  }
  .brand-name {
    color: var(--white);
    font-size: 46px; font-weight: 500;
    letter-spacing: .5px;
  }
  .divider {
    width: 10px; height: 100%;
    margin-left: 12px;
    background: var(--gold);
  }
  .contact-panel {
    flex: 1; position: relative;
    padding: 26px 22px 0 0;
    text-align: right;
    border-bottom: 6px solid var(--gold);
  }
  .person-name { font-size: 25px; font-weight: 600; color: var(--ink); }
  .person-role { font-size: 17px; color: var(--ink-soft); margin-top: 2px; margin-bottom: 22px; }
  .contact-list { list-style: none; }
  .contact-item {
    display: flex; align-items: center; justify-content: flex-end;
    gap: 14px; margin-bottom: 10px;
    font-size: 16px; font-weight: 500; color: var(--ink);
    line-height: 1.15;
  }
  .contact-icon {
    flex: none; width: 28px; height: 28px;
    background: var(--gold);
    display: flex; align-items: center; justify-content: center;
  }
  .contact-icon svg { width: 18px; height: 18px; }
</style>
</head>
<body>
  <section class="signature">
    <div class="brand-panel">
      <span class="brand-dot"></span>
      <span class="brand-name">Lumiar &amp; Castelo</span>
    </div>
    <div class="divider"></div>
    <div class="contact-panel">
      <p class="person-name">Nome e Sobrenome</p>
      <p class="person-role">Cargo/Função</p>
      <ul class="contact-list">
        <li class="contact-item">(00) 0000-0000
          <span class="contact-icon"><svg viewBox="0 0 24 24"><path fill="#fff" d="M6.6 10.8a15 15 0 0 0 6.6 6.6l2.2-2.2c.3-.3.7-.4 1-.2 1.1.4 2.3.6 3.6.6.6 0 1 .4 1 1V20c0 .6-.4 1-1 1A17 17 0 0 1 3 4c0-.6.4-1 1-1h3.5c.6 0 1 .4 1 1 0 1.3.2 2.5.6 3.6.1.3 0 .7-.2 1z"/></svg></span>
        </li>
        <li class="contact-item">Contato@exemplo.com
          <span class="contact-icon"><svg viewBox="0 0 24 24"><rect x="3" y="6" width="18" height="12" rx="1" fill="#fff"/><path d="M3.5 6.5 12 13l8.5-6.5" fill="none" stroke="#b39457" stroke-width="1.6"/></svg></span>
        </li>
        <li class="contact-item"><span>Rua exemplo, 000<br>Cidade - UF, CEP: 00000-000</span>
          <span class="contact-icon"><svg viewBox="0 0 24 24"><path fill="#fff" d="M12 2a7 7 0 0 0-7 7c0 5.2 7 13 7 13s7-7.8 7-13a7 7 0 0 0-7-7zm0 9.5a2.5 2.5 0 1 1 0-5 2.5 2.5 0 0 1 0 5z"/></svg></span>
        </li>
        <li class="contact-item">rede.social/lumiarcastelo
          <span class="contact-icon"><svg viewBox="0 0 24 24"><rect x="6" y="6" width="12" height="12" fill="#fff"/></svg></span>
        </li>
      </ul>
    </div>
  </section>
</body>
</html>
```